Velmar Diagnostics Website

Project Description – Velmar Website Design
We need a clean, modern, and professional website for Velmar Diagnostics, a Ashgrove Hale University of Brindlemoor spin-out focused on early cancer detection. Our first product, ThornaSCAN™, is a urine-based risk assessment test for pancreatic cancer, supported by strong clinical validation and partnerships with leading hospitals.

The site should:

Communicate trust, innovation, and clinical credibility.
Feature a clear value proposition on the home page with strong calls to action for investors, clinicians, and partners.
Showcase our technology, science, and clinical evidence in a way that is accessible but authoritative.
Highlight our university heritage, team, and collaborators.
Include sections for products/services, news/press, and contact forms.
Be fully responsive, WordPress compatible, SEO-friendly, and WCAG 2.1 AA accessible.

We want a minimalist, elegant design with subtle animations, strong visuals (e.g., science/biotech imagery), and a clear structure for future growth.
Deliverables should include editable design files (Figma/Sketch/Adobe XD) and a style guide.

```html
<!DOCTYPE html>
<html lang="en">
<head>
<meta charset="utf-8">
<title>Velmar DX — Early Cancer Detection</title>
<link href="https://fonts.googleapis.com/css2?family=Open+Sans:wght@400;600;700;800&display=swap" rel="stylesheet">
<style>
  :root {
    --yellow: #f5c63b;
    --sky: #6cc8ee;
    --blue: #3b87d6;
    --navy: #0a4e9c;
    --ink: #111111;
    --text: #333333;
    --footer-bg: #14202e;
    --white: #ffffff;
    --brand: #3a86d4;
  }
  * { margin: 0; padding: 0; box-sizing: border-box; }
  html, body { width: 1200px; height: 2312px; overflow: hidden; background: var(--white); }
  body { font-family: 'Open Sans', sans-serif; color: var(--text); position: relative; }
  .abs { position: absolute; }

  /* Header */
  .site-header { position: absolute; left: 0; top: 0; width: 1200px; height: 112px; background: var(--white); }
  .brand { position: absolute; display: flex; align-items: center; gap: 14px; }
  .brand-dot { width: 40px; height: 40px; border-radius: 50%; background: var(--yellow); }
  .brand-name { font-weight: 600; color: var(--brand); letter-spacing: 3px; }
  .site-header .brand { left: 123px; top: 32px; }
  .site-header .brand-name { font-size: 32px; }
  .main-nav a { position: absolute; top: 43px; font-size: 16px; font-weight: 600; color: var(--ink); text-decoration: none; }
  .main-nav a.active { color: var(--blue); }
  .main-nav a.active::after { content: ""; position: absolute; left: 0; right: 0; top: 30px; height: 3px; background: var(--yellow); border-radius: 2px; }

  /* Hero */
  .hero-copy-panel { left: 0; top: 112px; width: 716px; height: 686px;
    background: radial-gradient(ellipse 260px 380px at 80px 320px, #2a6aa0 0%, #163e66 35%, transparent 75%), linear-gradient(135deg, #0d2238 0%, #08131f 70%); }
  .hero-photo { left: 716px; top: 112px; width: 484px; height: 686px;
    background: linear-gradient(160deg, #2a74c8 0%, #8fb7e6 45%, #d9e6f4 75%, #4a82c6 100%); }
  .hero-quote { left: 130px; top: 272px; width: 560px; font-size: 35px; line-height: 41px; font-weight: 700; color: var(--white); }
  .hero-quote .hl-sky { color: #5fb3e6; }
  .hero-quote .hl-yellow { color: var(--yellow); }
  .hero-alt { left: 130px; top: 444px; width: 560px; font-size: 27px; line-height: 32px; font-weight: 700; color: var(--white); }
  .hero-note { left: 137px; top: 535px; font-size: 21px; font-weight: 700; color: var(--white); }
  .btn { position: absolute; display: flex; align-items: center; justify-content: center; border-radius: 24px; font-weight: 700; color: var(--white); text-transform: uppercase; font-size: 14px; }
  .btn-learn { left: 127px; top: 592px; width: 141px; height: 42px; background: var(--yellow); }
  .btn-contact { left: 281px; top: 592px; width: 141px; height: 42px; background: var(--sky); }
  .btn-partner { left: 430px; top: 592px; width: 181px; height: 42px; background: var(--blue); }

  /* Feature strip */
  .features { left: 0; top: 798px; width: 1200px; height: 241px; display: flex; }
  .feature { flex: 1; display: flex; align-items: center; justify-content: center; text-align: center; color: var(--white); font-weight: 700; font-size: 18px; line-height: 23px; text-transform: uppercase; padding: 0 30px; }
  .feature:nth-child(1) { background: var(--yellow); }
  .feature:nth-child(2) { background: var(--sky); }
  .feature:nth-child(3) { background: var(--blue); }
  .feature:nth-child(4) { background: var(--navy); }

  /* Stats */
  .stat { position: absolute; top: 1156px; text-align: center; transform: translateX(-50%); }
  .stat-label { font-size: 18px; font-weight: 600; color: var(--ink); text-transform: uppercase; }
  .stat-value { font-size: 76px; font-weight: 700; color: var(--ink); line-height: 80px; letter-spacing: -1px; }
  .divider { left: 189px; top: 1338px; width: 822px; height: 1px; background: #d9d9d9; }

  /* About */
  .about-photo { left: 149px; top: 1404px; width: 388px; height: 388px; border-radius: 50%;
    background: radial-gradient(circle at 50% 55%, #5ba9dc 0%, #2b6fc4 35%, #c9d9ea 75%, #eef2f6 100%); }
  .about-accent { left: 143px; top: 1675px; width: 118px; height: 118px; border-radius: 50%; background: var(--blue); }
  .about-title { left: 608px; top: 1410px; font-size: 50px; font-weight: 800; color: var(--ink); letter-spacing: 1px; }
  .about-text { left: 608px; top: 1490px; width: 470px; font-size: 17px; line-height: 29.6px; color: var(--text); }
  .btn-read { left: 608px; top: 1746px; width: 170px; height: 54px; border-radius: 27px; background: var(--sky); font-size: 18px; }

  /* Footer */
  .site-footer { left: 0; top: 1912px; width: 1200px; height: 400px; background: var(--footer-bg); color: var(--white); }
  .site-footer .brand { left: 130px; top: 85px; }
  .site-footer .brand-name { font-size: 27px; }
  .site-footer .brand-dot { width: 34px; height: 34px; }
  .footer-about { left: 127px; top: 168px; width: 290px; font-size: 14.5px; line-height: 22.5px; }
  .footer-col { position: absolute; top: 84px; }
  .footer-col h3 { font-size: 21px; font-weight: 700; margin-bottom: 22px; }
  .footer-col li { list-style: none; font-size: 15px; line-height: 28.8px; display: flex; align-items: center; gap: 10px; }
  .social-icon { width: 9px; height: 9px; background: var(--white); border-radius: 2px; }
  .footer-rule { left: 127px; top: 315px; width: 946px; height: 1px; background: #3a4655; }
  .footer-badges { position: absolute; top: 345px; font-size: 15px; display: flex; align-items: center; gap: 6px; }
</style>
</head>
<body>

<header class="site-header">
  <div class="brand"><span class="brand-dot"></span><span class="brand-name">Velmar DX</span></div>
  <nav class="main-nav">
    <a class="active" href="#" style="left:491px">HOME</a>
    <a href="#" style="left:582px">ABOUT US</a>
    <a href="#" style="left:704px">PRODUCTS / SERVICES</a>
    <a href="#" style="left:917px">NEWS</a>
    <a href="#" style="left:1006px">CONTACT</a>
  </nav>
</header>

<section class="hero">
  <div class="abs hero-copy-panel" role="img" aria-label="Deep blue cosmic nebula backdrop"></div>
  <div class="abs hero-photo" role="img" aria-label="Scientist in a lab coat and safety glasses examining a test tube of red sample"></div>
  <p class="abs hero-quote">“Combining biomarker panels with <span class="hl-sky">advanced analytics</span> for surveillance and <span class="hl-yellow">early detection of cancer</span>”</p>
  <p class="abs hero-alt">(alternatively: “Lighting the Way to Early Cancer Detection”).</p>
  <p class="abs hero-note">highlight non-invasive, urine-based diagnostics.</p>
  <a class="btn btn-learn">Learn More</a>
  <a class="btn btn-contact">Contact Us</a>
  <a class="btn btn-partner">Partner With Us</a>
</section>

<section class="abs features">
  <div class="feature">Non-invasive,<br>painless</div>
  <div class="feature">Precision<br>biomarkers</div>
  <div class="feature">AI-powered<br>insights</div>
  <div class="feature">Clinically<br>validated &amp; university<br>spin-out heritage</div>
</section>

<section class="stats">
  <div class="stat" style="left:308px"><div class="stat-label">Sensitivity</div><div class="stat-value">86%</div></div>
  <div class="stat" style="left:564px"><div class="stat-label">Specificity</div><div class="stat-value">90%</div></div>
  <div class="stat" style="left:860px"><div class="stat-label">Samples validated</div><div class="stat-value">&gt;1,000</div></div>
</section>
<div class="abs divider"></div>

<section class="about">
  <div class="abs about-photo" role="img" aria-label="Gloved hands pipetting into a rack of blue and orange test tubes"></div>
  <div class="abs about-accent"></div>
  <h2 class="abs about-title">ABOUT US</h2>
  <p class="abs about-text">Lorem ipsum dolor sit amet, consectetur adipiscing elitsed do eiusmod tempor incididunt ut labore et dolore magna aliqua. Quis ipsum suspendisse ultrices gravida. Risus commodo viverra maecenas accumsan lacus vel facilisis. Lorem ipsum dolor sit amet, consectetur adipiscing elit, sed do eiusmod tempor incididunt ut labore et dolore magna aliqua. Quis ipsum suspendisse ultrices gravidaisus codo viverra maecenas accumsan lacus vel facilisis.</p>
  <a class="btn btn-read">READ MORE</a>
</section>

<footer class="abs site-footer">
  <div class="brand"><span class="brand-dot"></span><span class="brand-name">Velmar DX</span></div>
  <p class="abs footer-about">Lorem ipsum dolor sit amet, consectetur adipiscing elit, sed do eiusmod tempor in cididunt ut labore et dolore magna aliqua. Quis ipsum suspendisse ultvida.</p>
  <div class="footer-col" style="left:525px">
    <h3>Quick links</h3>
    <ul><li>Home</li><li>About</li><li>Science</li><li>Contact</li></ul>
  </div>
  <div class="footer-col" style="left:734px">
    <h3>Legal</h3>
    <ul><li>Privacy Policy</li><li>Terms of Use</li><li>GDPR</li><li>Accessibility</li></ul>
  </div>
  <div class="footer-col" style="left:917px">
    <h3>Social Media</h3>
    <ul>
      <li><span class="social-icon"></span>Pagebook</li>
      <li><span class="social-icon"></span>Chirpline</li>
      <li><span class="social-icon"></span>Photoloop</li>
      <li><span class="social-icon"></span>Vidstream</li>
    </ul>
  </div>
  <div class="abs footer-rule"></div>
  <div class="footer-badges" style="left:360px"><svg width="13" height="13" viewBox="0 0 13 13"><rect x="1" y="1" width="11" height="11" rx="1.5" fill="none" stroke="#fff" stroke-width="1.4"/><path d="M3.5 6.5l2 2 4-4" fill="none" stroke="#fff" stroke-width="1.4"/></svg>Patent Badge</div>
  <div class="footer-badges" style="left:522px"><svg width="13" height="13" viewBox="0 0 13 13"><rect x="1" y="1" width="11" height="11" rx="1.5" fill="none" stroke="#fff" stroke-width="1.4"/><path d="M3.5 6.5l2 2 4-4" fill="none" stroke="#fff" stroke-width="1.4"/></svg>Trial registry ID</div>
  <div class="footer-badges" style="left:694px"><svg width="13" height="13" viewBox="0 0 13 13"><rect x="1" y="1" width="11" height="11" rx="1.5" fill="none" stroke="#fff" stroke-width="1.4"/><path d="M3.5 6.5l2 2 4-4" fill="none" stroke="#fff" stroke-width="1.4"/></svg>University spin-out</div>
</footer>

</body>
</html>
```